A clean crisp business card for a Landscape Construction company. Designed to be easy to read contact/ info and also be appealing/interesting, unlike a traditional business card.

Industry/Entity Type

Landscape Construction

Contact Information for Business Card

Company name : Bramblecrest Landscape Construction, phone number: (877) 62Vales, website:Bramblecrestlandscapes.example, Email, sales@bramblecrestlandscapes.example

Requirements
Nice to have
• Luxurious finishes/ details…. Icons or emblems next to contact info
Should not have
• Clipart or general pictures

```html
<!DOCTYPE html>
<html lang="en">
<head>
<meta charset="utf-8">
<title>Bramblecrest Landscape Construction — Business Card</title>
<link rel="stylesheet" href="https://fonts.googleapis.com/css2?family=Cinzel:wght@400;600&family=Arimo:wght@400&display=swap">
<style>
  :root {
    --backdrop: #3a302c;
    --card-black: #151515;
    --card-charcoal: #1e1e1e;
    --brand-blue: #2a78d0;
    --brand-green: #9acd32;
    --paper: #ffffff;
    --ink: #111111;
  }
  * { box-sizing: border-box; margin: 0; padding: 0; }
  html, body {
    width: 1200px; height: 716px; overflow: hidden;
    background: var(--backdrop);
  }
  .stage { position: relative; width: 1200px; height: 716px; }
  .card {
    position: absolute; top: 215px;
    width: 500px; height: 286px;
    border-bottom: 3px solid var(--brand-green);
    border-right: 2px solid var(--brand-green);
    box-shadow: 0 10px 24px rgba(0,0,0,.45);
    overflow: hidden;
  }
  .card--back { left: 70px; background: var(--card-charcoal); }
  .card--front { left: 630px; background: var(--card-black); }
  .card__waves { position: absolute; inset: 0; width: 100%; height: 100%; }

  .brand-name {
    position: absolute; text-align: center;
    font-family: "Cinzel", serif; font-weight: 600;
    color: var(--brand-blue);
    line-height: 1;
  }
  .brand-name__main { display: block; font-size: 34px; letter-spacing: 1px; }
  .brand-name__sub { display: block; font-size: 11px; letter-spacing: 4px; margin-top: 8px; }
  .card--back .brand-name { left: 0; right: 0; top: 112px; }
  .card--front .brand-name { left: 30px; width: 320px; top: 42px; }
  .card--front .brand-name__main { font-size: 30px; }
  .card--front .brand-name__sub { font-size: 10px; letter-spacing: 3px; }

  .person {
    position: absolute; right: 28px; top: 184px; text-align: right;
    font-family: "Cinzel", serif; line-height: 1.1;
  }
  .person__name { font-size: 21px; font-weight: 600; color: var(--brand-blue); letter-spacing: 1px; }
  .person__role { font-size: 12px; font-weight: 600; color: var(--brand-green); letter-spacing: 2px; margin-top: 2px; }

  .contacts {
    position: absolute; left: 170px; right: 28px; top: 234px;
    list-style: none;
    font-family: "Arimo", sans-serif; font-size: 11px; color: var(--ink);
  }
  .contacts__item {
    display: flex; justify-content: flex-end; align-items: center; gap: 6px;
    line-height: 15px;
  }
  .contacts__icon { width: 10px; height: 10px; flex: none; }
</style>
</head>
<body>
<main class="stage">

  <section class="card card--back" aria-label="Card back">
    <p class="brand-name">
      <span class="brand-name__main">Bramblecrest</span>
      <span class="brand-name__sub">LANDSCAPE CONSTRUCTION</span>
    </p>
  </section>

  <section class="card card--front" aria-label="Card front">
    <svg class="card__waves" viewBox="0 0 500 286" preserveAspectRatio="none" aria-hidden="true">
      <path fill="var(--brand-blue)" d="M0,92 C40,140 100,158 210,162 C150,168 60,162 0,118 Z"/>
      <path fill="var(--brand-green)" d="M0,118 C60,170 150,174 260,156 C360,140 440,130 500,96 L500,108 C440,144 360,154 260,168 C150,186 60,180 0,134 Z"/>
      <path fill="var(--paper)" d="M0,142 C60,192 150,194 260,176 C360,162 440,152 500,118 L500,286 L0,286 Z"/>
    </svg>

    <p class="brand-name">
      <span class="brand-name__main">Bramblecrest</span>
      <span class="brand-name__sub">LANDSCAPE CONSTRUCTION</span>
    </p>

    <div class="person">
      <p class="person__name">DANIEL HARLOW</p>
      <p class="person__role">DIRECTOR</p>
    </div>

    <ul class="contacts">
      <li class="contacts__item">(877) 62Vales
        <svg class="contacts__icon" viewBox="0 0 10 10" aria-hidden="true"><path d="M2,1 L4,1 L4.5,3 L3.3,4 C3.8,5.2 4.8,6.2 6,6.7 L7,5.5 L9,6 L9,8 C9,8.6 8.5,9 8,9 C4.5,9 1,5.5 1,2 C1,1.5 1.4,1 2,1 Z" fill="var(--brand-blue)"/></svg>
      </li>
      <li class="contacts__item">sales@bramblecrestlandscapes.example
        <svg class="contacts__icon" viewBox="0 0 10 10" aria-hidden="true"><rect x="1" y="2.5" width="8" height="5.5" fill="none" stroke="var(--brand-blue)" stroke-width="1"/><path d="M1,2.5 L5,5.5 L9,2.5" fill="none" stroke="var(--brand-blue)" stroke-width="1"/></svg>
      </li>
      <li class="contacts__item">www.bramblecrestlandscapes.example
        <svg class="contacts__icon" viewBox="0 0 10 10" aria-hidden="true"><g fill="none" stroke="var(--brand-blue)" stroke-width=".9"><circle cx="5" cy="5" r="4"/><ellipse cx="5" cy="5" rx="1.8" ry="4"/><path d="M1,5 H9 M1.6,3 H8.4 M1.6,7 H8.4"/></g></svg>
      </li>
    </ul>
  </section>

</main>
</body>
</html>
```